Business Card for Yachting Management Company

Need a business card design for a new yachting project management company. Attached is the logo for the company.
Our clients are large yacht owners and captains.
Design must be in the style of the logo. Modern, elegant.

Example of data to show:
Peter Hollis
Project Manager
(+34) 612 738 104
peter@quorvane.net
Quorvane Management - Meridel Tower, Office 22 - KRB - Salvena de Mar

The data above will have to be changed (by me) for the different people in the company over the next years.

Will be printed using PrintNova (Lustre Card Series). They provide these guidelines for the size:
"the actual size of the card is 1050 x 600 pixels. However, the full bleed size is 1083 x 633 pixels, and the safe printing area is 1008 x 558 pixels."

```html
<!DOCTYPE html>
<html lang="en">
<head>
<meta charset="utf-8">
<title>Quorvane Management – Business Card</title>
<link href="https://fonts.googleapis.com/css2?family=Open+Sans:wght@400;700&display=swap" rel="stylesheet">
<style>
  :root{
    --page:#dcdcdc;
    --card-white:#ffffff;
    --card-dark:#1b1b1c;
    --brand-blue:#1a72c0;
    --text-grey:#767676;
    --silver:#c9ccd2;
    --shadow:0 6px 18px rgba(0,0,0,.22);
  }
  *{box-sizing:border-box;margin:0;padding:0}
  html,body{width:1083px;height:1200px;overflow:hidden}
  body{
    background:var(--page);
    font-family:"Open Sans",Arial,sans-serif;
    position:relative;
  }
  .card{
    position:absolute;
    left:69px;
    width:945px;
    height:540px;
    box-shadow:var(--shadow);
    overflow:hidden;
  }
  .card--front{top:40px;background:var(--card-white)}
  .card--back{top:620px;background:var(--card-dark)}

  /* front */
  .brand{
    position:absolute;
    left:92px;
    top:76px;
    line-height:1.1;
  }
  .brand__name{
    display:block;font-size:54px;font-weight:700;color:var(--brand-blue);letter-spacing:.5px;
  }
  .brand__sub{
    display:block;font-size:21px;font-weight:400;color:var(--text-grey);
    letter-spacing:8.5px;margin-top:4px;
  }

  .person{
    position:absolute;
    right:90px;
    top:104px;
    text-align:right;
  }
  .person__name{
    font-size:40px;font-weight:700;color:var(--brand-blue);letter-spacing:.3px;line-height:1.1;
  }
  .person__role{
    font-size:25px;font-weight:700;color:var(--text-grey);margin-top:2px;letter-spacing:.3px;
  }

  .info{
    position:absolute;
    top:358px;
    font-size:25px;
    color:var(--text-grey);
    line-height:32px;
    list-style:none;
  }
  .info--address{left:90px}
  .info--contact{left:620px}
  .info li{position:relative;padding-left:30px}
  .icon{
    position:absolute;left:0;top:7px;width:18px;height:18px;fill:var(--brand-blue);
  }

  /* back */
  .texture{position:absolute;inset:0;background:var(--card-dark)}
  .back-brand{
    position:absolute;left:0;right:0;top:172px;text-align:center;line-height:1.1;
  }
  .back-brand__name{
    display:block;font-size:80px;font-weight:700;color:var(--brand-blue);letter-spacing:1px;
  }
  .back-brand__sub{
    display:block;font-size:30px;font-weight:400;color:var(--silver);
    letter-spacing:12px;margin-top:6px;padding-left:12px;
  }
</style>
</head>
<body>

<section class="card card--front" aria-label="Card front">
  <div class="brand">
    <span class="brand__name">Quorvane</span>
    <span class="brand__sub">MANAGEMENT</span>
  </div>

  <div class="person">
    <p class="person__name">PETER HOLLIS</p>
    <p class="person__role">Project Manager</p>
  </div>

  <ul class="info info--address">
    <li>
      <svg class="icon" viewBox="0 0 24 24" aria-hidden="true"><path d="M12 1a8 8 0 0 0-8 8c0 6 8 14 8 14s8-8 8-14a8 8 0 0 0-8-8zm0 11a3 3 0 1 1 0-6 3 3 0 0 1 0 6z"/></svg>
      Quorvane Management
    </li>
    <li>Meridel Tower, Office 22</li>
    <li>KRB - Salvena de Mar</li>
  </ul>

  <ul class="info info--contact">
    <li>
      <svg class="icon" viewBox="0 0 24 24" aria-hidden="true"><path d="M6.6 10.8a15 15 0 0 0 6.6 6.6l2.2-2.2c.3-.3.7-.4 1-.2 1.1.4 2.3.6 3.6.6.6 0 1 .4 1 1V20c0 .6-.4 1-1 1A17 17 0 0 1 3 4c0-.6.4-1 1-1h3.5c.6 0 1 .4 1 1 0 1.3.2 2.5.6 3.6.1.3 0 .7-.2 1z"/></svg>
      +34 612 738 104
    </li>
    <li>
      <svg class="icon" viewBox="0 0 24 24" aria-hidden="true"><path d="M2 5h20v14H2zm2 2v.5l8 5 8-5V7l-8 5z"/></svg>
      peter@quorvane.net
    </li>
    <li>
      <svg class="icon" viewBox="0 0 24 24" aria-hidden="true"><path d="M12 2a10 10 0 1 0 0 20 10 10 0 0 0 0-20zm6.9 6h-3a15 15 0 0 0-1.3-3.9A8 8 0 0 1 18.9 8zM12 4c.8 1.1 1.5 2.5 1.9 4h-3.8c.4-1.5 1.1-2.9 1.9-4zM4.3 14a8 8 0 0 1 0-4h3.4a16 16 0 0 0 0 4zm.8 2h3a15 15 0 0 0 1.3 3.9A8 8 0 0 1 5.1 16zm3-8h-3a8 8 0 0 1 4.3-3.9C8.8 5.3 8.4 6.6 8.1 8zM12 20c-.8-1.1-1.5-2.5-1.9-4h3.8c-.4 1.5-1.1 2.9-1.9 4zm2.3-6H9.7a14 14 0 0 1 0-4h4.6a14 14 0 0 1 0 4zm.3 5.9c.6-1.2 1-2.5 1.3-3.9h3a8 8 0 0 1-4.3 3.9zm1.7-5.9a16 16 0 0 0 0-4h3.4a8 8 0 0 1 0 4z"/></svg>
      www.quorvane.net
    </li>
  </ul>
</section>

<section class="card card--back" aria-label="Card back">
  <div class="texture" role="img" aria-label="Subtle dark repeating triangle texture across the card"></div>
  <div class="back-brand">
    <span class="back-brand__name">Quorvane</span>
    <span class="back-brand__sub">MANAGEMENT</span>
  </div>
</section>

</body>
</html>
```